Stationery Design Project for a consulting/educational company

We need a stationery design for a consulting / educational company called "VORT d.o.o.". We are an official partner (yet stand-alone company) of the MELQ Institute, Germany (www.melq-example.de) that covers practically all themes regarding production optimisation, efectiveness, productivity (time studies, workplace organisation,...) We need the design for:

- a CERTIFICATE for seminar participates
- business cards
- letterhead

We are changing our webpage to their design, so we need to change the stationaries as well. I included 2 current logos, one with current color scheme (not important) and the other black/white with a frame. I also included the MELQ original certificate. Only the font + name"VORT" is important, the rest is up to you
Updates

Designs look good, but perhaps a gray & green combo would look nicer? Like on www.melq-example.de? And without the frames?

Target Market(s)

Larger production companies top and middle management

Industry/Entity Type

Business

Requirements
Must have
• - the stationaries (all of them) should, besides the company name "VORT", also include the logo MELQ (in its color), like on their webpage www.melq-example.de
Nice to have
• - certificate could use 5th color (e.g. silver) to make an impression
- similar color scheme to www.melq-example.de

```html
<!DOCTYPE html>
<html lang="en">
<head>
<meta charset="utf-8">
<title>VORT business card</title>
<link href="https://fonts.googleapis.com/css2?family=Lato:wght@400;700&display=swap" rel="stylesheet">
<style>
  :root {
    --backdrop: #dfe3e5;
    --paper: #ffffff;
    --teal: #119fa6;
    --ink: #4a4a4a;
    --ink-soft: #5c5c5c;
    --rule: #6a6a6a;
    --tab: #6b6b6b;
  }
  * { box-sizing: border-box; margin: 0; padding: 0; }
  html, body {
    width: 1200px; height: 960px; overflow: hidden;
    background: var(--backdrop);
    font-family: "Lato", sans-serif;
  }
  .stage { position: relative; width: 1200px; height: 960px; }
  .card {
    position: absolute; left: 290px; width: 620px; height: 354px;
    box-shadow: 0 6px 18px rgba(0,0,0,.15);
  }
  .card-front { top: 70px; background: var(--paper); color: var(--ink); }
  .card-back { top: 500px; background: var(--teal); }

  .brand-name {
    position: absolute; top: 26px; left: 32px;
    font-size: 60px; font-weight: 700; letter-spacing: 4px; color: var(--ink);
  }
  .partner-name {
    position: absolute; top: 26px; left: 338px;
    font-size: 46px; font-weight: 700; letter-spacing: 2px; color: var(--ink);
  }
  .partner-band {
    position: absolute; top: 92px; left: 338px; width: 252px; height: 34px;
    background: var(--teal);
  }
  .person { position: absolute; top: 200px; left: 32px; }
  .person-name { font-size: 27px; color: var(--ink); }
  .person-role { font-size: 17px; color: var(--ink-soft); margin-top: 4px; }
  .divider {
    position: absolute; top: 258px; left: 32px; width: 558px; height: 1px;
    background: var(--rule);
  }
  .contacts {
    position: absolute; top: 272px; left: 32px; list-style: none;
    font-size: 17px; color: var(--ink); line-height: 25px;
  }
  .contacts li { display: flex; align-items: center; gap: 12px; }
  .contacts svg { width: 16px; height: 16px; flex: none; }
  .address {
    position: absolute; top: 270px; right: 30px; text-align: right;
    font-size: 14px; color: var(--ink-soft); line-height: 20px;
  }
  .address .web { font-weight: 700; color: var(--ink); }

  .back-name {
    position: absolute; inset: 0;
    display: flex; align-items: center; justify-content: center;
    font-size: 92px; font-weight: 700; letter-spacing: 8px; color: var(--paper);
  }
  .back-tab {
    position: absolute; top: 22px; left: 0; width: 16px; height: 16px;
    background: var(--tab);
  }
</style>
</head>
<body>
<main class="stage">
  <section class="card card-front" aria-label="Business card front">
    <div class="brand-name">VORT</div>
    <div class="partner-name">MELQ</div>
    <div class="partner-band"></div>

    <div class="person">
      <p class="person-name">Name Surname</p>
      <p class="person-role">Operation Manager</p>
    </div>
    <div class="divider"></div>

    <ul class="contacts">
      <li>
        <svg viewBox="0 0 16 16" aria-hidden="true"><rect x="1.5" y="1.5" width="13" height="13" rx="2" fill="none" stroke="var(--teal)" stroke-width="1.6"/><rect x="4" y="4" width="3" height="8" fill="var(--teal)"/><rect x="9" y="4" width="3.5" height="2" fill="var(--teal)"/><rect x="9" y="8" width="3.5" height="4" fill="var(--teal)"/></svg>
        (221) 33 000 12 34
      </li>
      <li>
        <svg viewBox="0 0 16 16" aria-hidden="true"><rect x="4" y="1.5" width="8" height="4" fill="var(--teal)"/><rect x="1.5" y="6" width="13" height="6" rx="1.5" fill="var(--teal)"/><rect x="4" y="10" width="8" height="4.5" fill="var(--paper)" stroke="var(--teal)" stroke-width="1.4"/></svg>
        (221) 33 000 56 78
      </li>
      <li>
        <svg viewBox="0 0 16 16" aria-hidden="true"><rect x="1.5" y="3.5" width="13" height="9" fill="none" stroke="var(--teal)" stroke-width="1.6"/><path d="M1.5 3.5 8 9l6.5-5.5" fill="none" stroke="var(--teal)" stroke-width="1.6"/></svg>
        name@vort-example.com
      </li>
    </ul>

    <address class="address">
      Avenue des Lilas - Beau Site<br>
      BP 120 - City, Country<br>
      <span class="web">www.vort-example.com</span>
    </address>
  </section>

  <section class="card card-back" aria-label="Business card back">
    <div class="back-tab"></div>
    <div class="back-name">VORT</div>
  </section>
</main>
</body>
</html>
```